Marigold’s family restaurant & ice cream parlor

Looking for something that matches an old fashion vintage look for a family run business in an historic downtown district that is a unique nostalgic dining experience
With lots of memorabilia

Target Market(s)

Families

Industry/Entity Type

Diner , restaurant

Contact Information for Business Card

Picture of a Steam engine locomotive , ice cream cones, chalkboard look , black background

Font styles to use
Serif
Decorative

Colors

Designer to choose colors to be used in the design.

```html
<!DOCTYPE html>
<html lang="en">
<head>
<meta charset="utf-8">
<title>Marigold’s Family Restaurant &amp; Ice Cream Parlor – Business Card</title>
<link rel="stylesheet" href="https://fonts.googleapis.com/css2?family=Rye&family=Oswald:wght@300;400;500&display=swap">
<style>
  :root {
    --backdrop: #ababab;
    --chalkboard: #2b2b2b;
    --chalkboard-light: #363636;
    --chalk-dust: rgba(220, 220, 220, 0.06);
    --chalk-smudge: rgba(200, 200, 200, 0.05);
    --chalk: #dcdcdc;
    --chalk-dim: #bdbdbd;
    --mint: #8fbab5;
    --cone: #d9b46a;
    --scoop: #4f7f80;
    --orange: #d9845a;
    --butter: #e6c36a;
    --rose: #c48a9c;
    --badge-navy: #1e4a6c;
    --badge-gold: #d8b25a;
  }
  * { box-sizing: border-box; margin: 0; padding: 0; }
  html, body {
    width: 1200px; height: 1000px; overflow: hidden;
    background: var(--backdrop);
  }
  .business-card {
    position: absolute; left: 291px; top: 324px;
    width: 618px; height: 350px;
    background: radial-gradient(ellipse at 50% 40%, var(--chalkboard-light), var(--chalkboard) 75%);
    color: var(--chalk);
    overflow: hidden;
  }
  .chalk-texture {
    position: absolute; inset: 0; pointer-events: none;
    background:
      radial-gradient(ellipse 120px 60px at 18% 22%, var(--chalk-smudge), transparent 70%),
      radial-gradient(ellipse 160px 70px at 78% 30%, var(--chalk-smudge), transparent 70%),
      radial-gradient(ellipse 140px 50px at 40% 80%, var(--chalk-smudge), transparent 70%),
      radial-gradient(ellipse 90px 90px at 90% 85%, var(--chalk-smudge), transparent 70%),
      repeating-linear-gradient(93deg, var(--chalk-dust) 0 1px, transparent 1px 7px),
      repeating-linear-gradient(2deg, transparent 0 5px, var(--chalk-dust) 5px 6px, transparent 6px 13px);
  }
  .card-frame {
    position: absolute; inset: 8px;
    border: 3px double var(--chalk-dim);
  }
  .arch-heading { position: absolute; left: 0; top: 0; width: 618px; height: 120px; }
  .arch-heading text {
    font-family: "Rye", serif; font-size: 18px; letter-spacing: 4px; fill: var(--chalk);
  }
  .established {
    position: absolute; top: 92px; font-family: "Oswald", sans-serif;
    font-size: 12px; letter-spacing: 1px; color: var(--chalk-dim);
  }
  .established.year-label { left: 234px; }
  .established.year-value { left: 350px; }
  .locomotive-art {
    position: absolute; left: 266px; top: 76px; width: 80px; height: 42px;
    background: linear-gradient(#cfcfcf, #8f8f8f); border-radius: 4px; opacity: .8;
  }
  .brand-name {
    position: absolute; left: 0; width: 100%; top: 118px; text-align: center;
    font-family: "Rye", serif; font-weight: 400; font-size: 50px; line-height: 1;
    color: var(--chalk); text-transform: uppercase;
    transform: scaleY(1.35); transform-origin: top center;
  }
  .parlor-line {
    position: absolute; left: 0; width: 100%; top: 202px; text-align: center;
    font-family: "Oswald", sans-serif; font-weight: 400; font-size: 25px;
    letter-spacing: 3px; color: var(--mint); text-transform: uppercase;
  }
  .meals-line {
    position: absolute; left: 0; width: 100%; top: 236px; text-align: center;
    font-family: "Oswald", sans-serif; font-weight: 500; font-size: 15px;
    letter-spacing: 1px; text-transform: uppercase; color: var(--chalk-dim);
  }
  .meal-breakfast { color: var(--orange); }
  .meal-lunch { color: var(--butter); }
  .meal-dinner { color: var(--rose); }
  .cone-art {
    position: absolute; top: 213px; width: 38px; height: 42px; border-radius: 4px;
    background: linear-gradient(var(--scoop), var(--cone));
  }
  .cone-art.left { left: 156px; }
  .cone-art.right { left: 432px; }
  .state-badge {
    position: absolute; left: 502px; top: 180px; width: 80px; height: 80px;
    border-radius: 50%; background: var(--badge-navy); border: 3px solid var(--badge-gold);
  }
  .divider-row {
    position: absolute; left: 89px; top: 275px; width: 450px;
    border-top: 3px dotted var(--chalk-dim);
  }
  .divider-col {
    position: absolute; left: 308px; top: 283px; height: 50px;
    border-left: 3px dotted var(--chalk-dim);
  }
  .contact-phone {
    position: absolute; left: 88px; top: 292px; display: flex; align-items: center; gap: 6px;
    font-family: "Oswald", sans-serif; font-weight: 300; font-size: 24px;
    letter-spacing: 1px; color: var(--chalk);
  }
  .contact-address {
    position: absolute; left: 328px; top: 284px;
    font-family: "Oswald", sans-serif; font-weight: 400; font-size: 15px;
    line-height: 22px; letter-spacing: .5px; text-transform: uppercase; color: var(--chalk);
  }
</style>
</head>
<body>
  <main class="business-card">
    <div class="chalk-texture"></div>
    <div class="card-frame"></div>

    <svg class="arch-heading" viewBox="0 0 618 120" aria-label="Family Restaurant">
      <path id="arch-path" d="M 165 98 Q 309 30 458 98" fill="none"/>
      <text><textPath href="#arch-path" startOffset="50%" text-anchor="middle">FAMILY RESTAURANT</textPath></text>
    </svg>

    <span class="established year-label">EST.</span>
    <div class="locomotive-art" role="img" aria-label="Steam locomotive illustration"></div>
    <span class="established year-value">1998</span>

    <h1 class="brand-name">Marigold’s</h1>

    <div class="cone-art left" role="img" aria-label="Ice cream cone illustration"></div>
    <p class="parlor-line">Ice Cream Parlor</p>
    <div class="cone-art right" role="img" aria-label="Ice cream cone illustration"></div>

    <p class="meals-line">
      <span class="meal-breakfast">Breakfast</span> •
      <span class="meal-lunch">Lunch</span> •
      <span class="meal-dinner">Dinner</span>
    </p>

    <div class="state-badge" role="img" aria-label="State badge"></div>

    <div class="divider-row"></div>
    <div class="divider-col"></div>

    <p class="contact-phone">
      <svg width="24" height="20" viewBox="0 0 24 20" aria-hidden="true">
        <path d="M2 7 Q12 0 22 7 L20 10 L16 8 L16 6 Q12 5 8 6 L8 8 L4 10 Z" fill="var(--chalk)"/>
        <rect x="5" y="10" width="14" height="9" rx="2" fill="var(--chalk)"/>
      </svg>
      (248) 555-0142
    </p>
    <p class="contact-address">218 Maple Grove Street,<br>Fairhaven, Michigan 48000</p>
  </main>
</body>
</html>
```